Redesign of an existing homepage

This site needs a redesign
https://www.ferien-am-haldbach.de
This page with the accommodation options is important for the customer
https://www.ferien-am-haldbach.de/gastgeber/
Till now there is a new logo. See attachment. That's all I have.
It would make sense to use the colors of the logo in the redesign.
footer.jpg.
I would put this info into the footer. The graphic (Infomaterial) is not needed.
a new menu - links.jpg
This info can be put in a new menu. Therefore the right column is gone and there is more space for the design.
NEW:
Please keep in mind that the Icons are important and shall be displayed under every accommodation
Number of Pages Required
1 page

```html
<!DOCTYPE html>
<html lang="en">
<head>
<meta charset="utf-8">
<title>Tourismusverband Haldbach – Holiday in the Rottal</title>
<link rel="stylesheet" href="https://fonts.googleapis.com/css2?family=Teko:wght@400;500;600&family=Poppins:wght@400;500;600&display=swap">
<style>
:root{
  --blue:#1f8fd3;
  --blue-dark:#0b5c93;
  --navy:#0a4a78;
  --green:#86c23f;
  --green-dark:#5c9a26;
  --ink:#2b2f36;
  --muted:#6b7380;
  --pale:#f3f6f8;
  --white:#ffffff;
  --head:"Teko",sans-serif;
  --body:"Poppins",sans-serif;
}
*{box-sizing:border-box;margin:0;padding:0}
html,body{width:1200px;height:4900px;overflow:hidden}
body{font-family:var(--body);color:var(--ink);background:var(--white);font-size:14px;line-height:1.6;position:relative}
a{color:inherit;text-decoration:none}
.section-title{font-family:var(--head);font-weight:500;font-size:52px;line-height:1;text-align:center;letter-spacing:1px;color:var(--ink)}
.btn{display:inline-block;background:var(--blue);color:var(--white);font-family:var(--head);font-size:20px;letter-spacing:1px;padding:10px 30px 6px;border-radius:30px;box-shadow:0 6px 14px rgba(31,143,211,.35)}
.center{text-align:center}

/* top bar */
.topbar{height:32px;background:var(--blue-dark);color:#d8ecf9;font-size:12px;display:flex;align-items:center;justify-content:space-between;padding:0 40px}
.topbar nav a{margin-right:22px}
/* header */
.header{height:72px;display:flex;align-items:center;justify-content:space-between;padding:0 40px;background:var(--white)}
.brand{display:flex;align-items:center;gap:12px}
.brand-dot{width:40px;height:40px;border-radius:50%;background:var(--blue)}
.brand-name{font-family:var(--head);font-size:24px;font-weight:500;line-height:1;color:var(--blue-dark)}
.main-nav{display:flex;gap:30px;font-family:var(--head);font-size:19px;letter-spacing:.5px;color:var(--ink)}
.main-nav a:first-child{color:var(--blue)}
.phone-btn{background:var(--green);color:var(--white);border-radius:24px;padding:8px 18px;font-size:13px;font-weight:600;display:flex;align-items:center;gap:8px}

/* hero */
.hero{position:relative;height:780px;background:linear-gradient(120deg,#c9e0b0 0%,#8fb865 30%,#5d8a3a 60%,#c8b88c 100%);overflow:hidden}
.hero-text{position:absolute;left:60px;top:180px;width:470px;color:var(--white)}
.hero-text h1{font-family:var(--head);font-weight:600;font-size:66px;line-height:.95;text-shadow:0 2px 8px rgba(0,0,0,.3)}
.hero-text h1 span{color:var(--blue)}
.hero-text p{margin-top:16px;font-size:14px;width:360px;text-shadow:0 1px 4px rgba(0,0,0,.4)}
.hero-wave{position:absolute;left:0;bottom:0;width:1200px;height:180px}

/* intro */
.intro{height:380px;display:flex;align-items:center;padding:0 120px 0 160px;gap:90px}
.intro-mark{width:320px;height:320px;border-radius:50%;background:#eaf4fb;display:flex;align-items:center;justify-content:center;flex-shrink:0}
.intro-mark span{font-family:var(--head);font-size:34px;font-weight:500;color:var(--blue-dark);text-align:center;line-height:1}
.intro-copy h2{font-family:var(--head);font-weight:500;font-size:52px;line-height:1;margin-bottom:14px}
.intro-copy p{font-size:13px;color:var(--muted);margin-bottom:12px}

/* tree band */
.treeline{height:180px;background:linear-gradient(180deg,#ffffff 0%,#9fc46a 35%,#5e8b34 70%,#e8efe0 100%)}

/* hosts */
.hosts{height:840px;background:var(--pale);padding-top:50px}
.host-grid{display:flex;justify-content:center;gap:30px;margin-top:50px}
.host-card{width:340px;height:600px;background:var(--white);border-radius:14px;box-shadow:0 10px 28px rgba(0,0,0,.12);overflow:hidden}
.host-photo{height:210px;position:relative}
.host-badge{position:absolute;left:14px;bottom:14px;width:110px;height:24px;border-radius:12px;background:rgba(10,74,120,.85)}
.host-body{padding:22px 24px}
.host-body h3{font-family:var(--head);font-weight:500;font-size:34px;line-height:1}
.host-addr{font-size:11px;color:var(--muted);letter-spacing:.5px;text-transform:uppercase}
.host-price{font-family:var(--head);font-size:24px;color:var(--green-dark);margin:10px 0 6px}
.host-body p{font-size:12.5px;color:var(--muted);height:118px}
.host-icons{display:flex;gap:10px;margin:14px 0;justify-content:center}
.host-icons span{width:28px;height:28px;border-radius:50%;border:2px solid var(--blue);display:flex;align-items:center;justify-content:center}
.host-link{display:block;text-align:center;border-top:1px solid #e3e7ec;padding-top:12px;font-size:12.5px;color:var(--blue);text-decoration:underline}
.hosts .center{margin-top:36px}

/* video */
.video{position:relative;height:900px;padding-top:20px}
.video-bg{position:absolute;left:0;top:0;width:1200px;height:900px}
.video-inner{position:relative;text-align:center}
.video-mark{width:90px;height:90px;border-radius:50%;background:var(--green);margin:60px auto 0}
.video h2{font-family:var(--head);font-weight:500;font-size:50px;line-height:1;color:var(--white);margin-top:34px}
.video-frame{position:relative;width:860px;height:480px;margin:30px auto 0;border-radius:24px;overflow:hidden;background:linear-gradient(180deg,#a9c9de 0%,#9cc26a 45%,#6f9f3e 100%);box-shadow:0 14px 30px rgba(0,0,0,.25)}
.play{position:absolute;left:50%;top:50%;width:70px;height:70px;margin:-35px 0 0 -35px;border-radius:50%;background:var(--white);display:flex;align-items:center;justify-content:center}

/* leisure */
.leisure{height:540px;padding-top:30px}
.leisure-list{display:flex;justify-content:center;gap:44px;margin-top:60px}
.leisure-item{width:130px;text-align:center;font-family:var(--head);font-size:20px;letter-spacing:.5px}
.leisure-circle{width:130px;height:130px;border-radius:50%;background:var(--white);box-shadow:0 8px 22px rgba(0,0,0,.12);display:flex;align-items:center;justify-content:center;margin-bottom:14px}
.leisure-circle.is-active{background:var(--green)}
.leisure-glyph{width:54px;height:54px;border-radius:50%;background:#d6ebf8}
.is-active .leisure-glyph{background:#c9e6a4}
.leisure .center{margin-top:56px}

/* news */
.news{height:600px;padding-top:40px}
.news-grid{display:flex;justify-content:center;gap:30px;margin-top:50px}
.news-card{width:340px;height:340px;background:var(--white);border-radius:14px;box-shadow:0 10px 28px rgba(0,0,0,.12);overflow:hidden}
.news-photo{height:170px}
.news-body{padding:18px 24px}
.news-body h3{font-family:var(--head);font-weight:500;font-size:24px;line-height:1.05}
.news-date{font-size:11px;color:var(--muted);margin:8px 0 6px;display:flex;align-items:center;gap:6px}
.news-body p{font-size:12px;color:var(--muted)}
.news-more{font-size:12px;color:var(--blue);font-weight:600;text-transform:uppercase}
.dots{display:flex;justify-content:center;gap:8px;margin-top:30px}
.dots span{width:20px;height:4px;background:#cfd6dd;border-radius:2px}
.dots span:nth-child(2){background:var(--blue);width:30px}

/* footer */
.footer-wave{height:180px;position:relative}
.footer-wave svg{position:absolute;left:0;top:0}
.footer{height:360px;background:var(--navy);color:#d7e6f2;position:relative}
.footer-cols{display:flex;padding:40px 100px 0 120px;gap:70px}
.footer-brand{width:250px;display:flex;flex-direction:column;align-items:center;gap:10px;padding-top:10px}
.footer-brand .brand-dot{width:70px;height:70px;background:var(--green)}
.footer-brand .brand-name{color:var(--white);font-size:26px;text-align:center}
.footer h4{font-family:var(--head);font-weight:500;font-size:26px;color:var(--white);margin-bottom:8px;letter-spacing:.5px}
.footer ul{list-style:none;font-size:12.5px;line-height:1.9}
.contact-row{display:flex;gap:10px;font-size:12px;margin-bottom:12px;line-height:1.5}
.contact-row svg{flex-shrink:0;margin-top:2px}
.hours{font-size:12.5px;line-height:1.9}
.footer-bottom{position:absolute;left:0;bottom:0;width:1200px;height:44px;background:#083d63;display:flex;align-items:center;justify-content:center;font-size:12px;color:#b8cfe1}
.footer-bottom .legal{position:absolute;right:60px}
</style>
</head>
<body>

<div class="topbar">
  <nav><a href="#">Haldbach</a><a href="#">Town Hall</a><a href="#">City Map</a><a href="#">Tourismusverband</a><a href="#">Gallery</a></nav>
  <span>Mon – Fri 8:00 – 17:00</span>
</div>

<header class="header">
  <div class="brand"><span class="brand-dot"></span><span class="brand-name">TOURISMUSVERBAND<br>HALDBACH</span></div>
  <nav class="main-nav"><a href="#">HOST</a><a href="#">ROTTAL</a><a href="#">LEISURE TIME</a><a href="#">EXCURSION DESTINATIONS</a><a href="#">ART AND CULTURE</a><a href="#">CONTACT</a></nav>
  <a class="phone-btn" href="#"><svg width="14" height="14" viewBox="0 0 24 24" fill="#fff"><path d="M6.6 10.8a15 15 0 0 0 6.6 6.6l2.2-2.2a1 1 0 0 1 1-.25 11.4 11.4 0 0 0 3.6.57 1 1 0 0 1 1 1V20a1 1 0 0 1-1 1A17 17 0 0 1 3 4a1 1 0 0 1 1-1h3.5a1 1 0 0 1 1 1c0 1.25.2 2.45.57 3.6a1 1 0 0 1-.25 1z"/></svg>+49 (0)1234 / 567 890</a>
</header>

<section class="hero" role="img" aria-label="Family cycling along a sunny country path lined with trees">
  <div class="hero-text">
    <h1>HOLIDAY IN THE <span>ROTTAL</span> – THE MOST BEAUTIFUL SPOT IN BAVARIA</h1>
    <p>Haldbach and the surrounding area have everything that makes life worth living.</p>
  </div>
  <svg class="hero-wave" viewBox="0 0 1200 180" preserveAspectRatio="none">
    <path d="M0 60 C300 170 800 40 1200 110 L1200 180 L0 180Z" fill="var(--green)"/>
    <path d="M0 90 C320 180 820 70 1200 135 L1200 180 L0 180Z" fill="var(--blue)"/>
    <path d="M0 120 C340 190 840 100 1200 160 L1200 180 L0 180Z" fill="#fff"/>
  </svg>
</section>

<section class="intro">
  <div class="intro-mark"><span>TOURISMUSVERBAND<br>HALDBACH</span></div>
  <div class="intro-copy">
    <h2>DEAR VISITORS</h2>
    <p>Dear visitors, Haldbach and the surrounding area have everything that makes life worth living: culture and nature, pleasure and enjoyment, friendly and open-minded people.</p>
    <p>Whether churches, fountains or other architectural monuments on a tour through the historic town, you can discover many loving details for yourself.</p>
    <p>For those who enjoy exercise and those seeking relaxation, there's "pure nature" in and around Haldbach. Here you can enjoy cycling, walking, hiking, golfing, horseback riding and swimming, or simply enjoy the peace and quiet.</p>
    <a class="btn" href="#">READ MORE</a>
  </div>
</section>

<div class="treeline" role="img" aria-label="Row of green deciduous trees under a pale sky"></div>

<section class="hosts">
  <h2 class="section-title">HOST IN THE ROTTAL</h2>
  <div class="host-grid">
    <article class="host-card">
      <div class="host-photo" role="img" aria-label="Farmhouse with wooden balconies and flowers" style="background:linear-gradient(160deg,#b9d4e6,#a08160 55%,#6f9a45)"><span class="host-badge"></span></div>
      <div class="host-body">
        <h3>FERIENHOF LINDNER</h3>
        <div class="host-addr">Wiesenweg 5, 12345 Haldbach</div>
        <div class="host-price">From € 70.00 for 4 people</div>
        <p>Our holiday farm in a quiet, idyllic location offers many recreational opportunities, such as walking, cycling and simply relaxing in the garden.</p>
        <div class="host-icons"><span></span><span></span><span></span><span></span><span></span></div>
        <a class="host-link" href="#">Our homepage von Ferienhof Lindner</a>
      </div>
    </article>
    <article class="host-card">
      <div class="host-photo" role="img" aria-label="Green meadow with farm buildings and visitors" style="background:linear-gradient(160deg,#c5dcea,#86b35a 55%,#55803a)"><span class="host-badge"></span></div>
      <div class="host-body">
        <h3>MOOSAUERHOF</h3>
        <div class="host-addr">Moosau 7, 12345 Haldbach</div>
        <div class="host-price">From € 70.00 for 4 people</div>
        <p>Simply everyday life can pause again. Enjoy an organic farm holiday with animals and nature close by, ideal for families and children.</p>
        <div class="host-icons"><span></span><span></span><span></span><span></span><span></span></div>
        <a class="host-link" href="#">Our homepage von Moosauerhof</a>
      </div>
    </article>
    <article class="host-card">
      <div class="host-photo" role="img" aria-label="Traditional Bavarian house with wooden balcony" style="background:linear-gradient(160deg,#bcd6ea,#c9a779 55%,#7fa552)"><span class="host-badge"></span></div>
      <div class="host-body">
        <h3>KRAMERHÄUSL</h3>
        <div class="host-addr">Kirchweg 3, 12345 Haldbach</div>
        <div class="host-price">From € 70.00 for 4 people</div>
        <p>An unforgettable, relaxing and peaceful holiday for the whole family awaits you here. Our cosy house lies right on the edge of the village.</p>
        <div class="host-icons"><span></span><span></span><span></span><span></span><span></span></div>
        <a class="host-link" href="#">Further information</a>
      </div>
    </article>
  </div>
  <div class="center"><a class="btn" href="#">VIEW ALL ROTTAL</a></div>
</section>

<section class="video">
  <svg class="video-bg" viewBox="0 0 1200 900" preserveAspectRatio="none">
    <path d="M0 60 C300 0 700 160 1200 40 L1200 760 C800 880 400 700 0 820Z" fill="var(--green)"/>
    <path d="M0 760 C400 660 800 860 1200 740 L1200 790 C800 900 400 710 0 810Z" fill="var(--blue)"/>
  </svg>
  <div class="video-inner">
    <div class="video-mark"></div>
    <h2>FREMDENVERKEHRSVEREIN<br>HALDBACH VIDEO</h2>
    <div class="video-frame" role="img" aria-label="Children riding horses across a green meadow">
      <span class="play"><svg width="24" height="24" viewBox="0 0 24 24"><path d="M7 4l13 8-13 8z" fill="var(--ink)"/></svg></span>
    </div>
  </div>
</section>

<section class="leisure">
  <h2 class="section-title">LEISURE IN THE ROTTAL</h2>
  <div class="leisure-list">
    <div class="leisure-item"><div class="leisure-circle" role="img" aria-label="Fishing icon"><span class="leisure-glyph"></span></div>FISHING</div>
    <div class="leisure-item"><div class="leisure-circle" role="img" aria-label="Hot air balloon icon"><span class="leisure-glyph"></span></div>BALLOON RIDES</div>
    <div class="leisure-item"><div class="leisure-circle" role="img" aria-label="Golf icon"><span class="leisure-glyph"></span></div>GOLF</div>
    <div class="leisure-item"><div class="leisure-circle" role="img" aria-label="Gastronomy icon"><span class="leisure-glyph"></span></div>GASTRONOMY</div>
    <div class="leisure-item"><div class="leisure-circle is-active" role="img" aria-label="Horse riding icon"><span class="leisure-glyph"></span></div>RIDE</div>
    <div class="leisure-item"><div class="leisure-circle" role="img" aria-label="Outdoor pool icon"><span class="leisure-glyph"></span></div>OUTDOOR POOLS</div>
  </div>
  <div class="center"><a class="btn" href="#">VIEW ALL</a></div>
</section>

<section class="news">
  <h2 class="section-title">LATEST NEWS &amp; EVENTS</h2>
  <div class="news-grid">
    <article class="news-card">
      <div class="news-photo" role="img" aria-label="Deer grazing in a wildlife park" style="background:linear-gradient(160deg,#7fa14c,#a37a4a)"></div>
      <div class="news-body"><h3>SOME BLOG HEADING GOES HERE WITH DES...</h3><div class="news-date">◷ 20-05-2024</div><p>We build long-term relationships, not one-off projects offering.</p><a class="news-more" href="#">Read more</a></div>
    </article>
    <article class="news-card">
      <div class="news-photo" role="img" aria-label="Garden with small wooden cabin" style="background:linear-gradient(160deg,#6d8f47,#9bbc6c)"></div>
      <div class="news-body"><h3>SOME BLOG HEADING GOES HERE WITH DES...</h3><div class="news-date">◷ 20-05-2024</div><p>We build long-term relationships, not one-off projects offering.</p><a class="news-more" href="#">Read more</a></div>
    </article>
    <article class="news-card">
      <div class="news-photo" role="img" aria-label="Beer garden tables under leafy trees" style="background:linear-gradient(160deg,#9cba6b,#a88b62)"></div>
      <div class="news-body"><h3>SOME BLOG HEADING GOES HERE WITH DES...</h3><div class="news-date">◷ 20-05-2024</div><p>We build long-term relationships, not one-off projects offering.</p><a class="news-more" href="#">Read more</a></div>
    </article>
  </div>
  <div class="dots"><span></span><span></span><span></span></div>
</section>

<div class="footer-wave">
  <svg width="1200" height="180" viewBox="0 0 1200 180" preserveAspectRatio="none">
    <path d="M0 110 C300 40 800 150 1200 60 L1200 180 L0 180Z" fill="var(--green)"/>
    <path d="M0 135 C320 70 820 170 1200 95 L1200 180 L0 180Z" fill="var(--blue)"/>
    <path d="M0 160 C340 110 840 180 1200 130 L1200 180 L0 180Z" fill="var(--navy)"/>
  </svg>
</div>

<footer class="footer">
  <div class="footer-cols">
    <div class="footer-brand"><span class="brand-dot"></span><span class="brand-name">TOURISMUSVERBAND<br>HALDBACH</span></div>
    <div>
      <h4>QUICK LINKS</h4>
      <ul><li>Home</li><li>Host</li><li>Rottal</li><li>Leisure time</li><li>Excursion destinations</li><li>Art and Culture</li><li>Contact</li></ul>
    </div>
    <div>
      <h4>CONTACT</h4>
      <div class="contact-row"><svg width="14" height="14" viewBox="0 0 24 24" fill="var(--green)"><path d="M6.6 10.8a15 15 0 0 0 6.6 6.6l2.2-2.2a1 1 0 0 1 1-.25 11.4 11.4 0 0 0 3.6.57 1 1 0 0 1 1 1V20a1 1 0 0 1-1 1A17 17 0 0 1 3 4a1 1 0 0 1 1-1h3.5a1 1 0 0 1 1 1c0 1.25.2 2.45.57 3.6a1 1 0 0 1-.25 1z"/></svg><span>Telephone<br>01234 / 567 890<br>01234 / 567 891</span></div>
      <div class="contact-row"><svg width="14" height="14" viewBox="0 0 24 24" fill="var(--green)"><path d="M2 5h20v14H2z M2 5l10 8 10-8" stroke="#0a4a78" stroke-width="1.5"/></svg><span>Email<br>info@ferien-am-haldbach.de</span></div>
    </div>
    <div>
      <h4>OPENING HOURS</h4>
      <div class="hours">Mon–Fri: 8:00 – 17:00<br>Sat–Sun: 9:00 – 12:00</div>
      <div class="contact-row" style="margin-top:14px"><svg width="14" height="14" viewBox="0 0 24 24" fill="var(--green)"><path d="M12 2a7 7 0 0 0-7 7c0 5 7 13 7 13s7-8 7-13a7 7 0 0 0-7-7zm0 9.5A2.5 2.5 0 1 1 12 6.5a2.5 2.5 0 0 1 0 5z"/></svg><span>Tourist Association of Haldbach<br>and surrounding area<br>Marktstraße 4, 12345 Haldbach</span></div>
    </div>
  </div>
  <div class="footer-bottom">Copyright 2024, Tourismusverband Haldbach, All Rights Reserved<span class="legal">Privacy Policy | Terms &amp; Conditions</span></div>
</footer>

</body>
</html>
```